Medical software helping patients with dry eye disease needs a business card

We have a logo we just need a design for a business card for a Canadian company called LUMA: Dry Eye. We use AI technology to assist optometrists in properly diagnosing patients with dry eye disease reducing wait times in doctors offices and accuracy of diagnosis as well as identifying key possible indicators and tailored treatment plans. The final design should be clean and medical looking. Our mission is to help patients and our logo using blues and whites.

```html
<!DOCTYPE html>
<html lang="en">
<head>
<meta charset="UTF-8">
<title>LUMA: Dry Eye — Business Card</title>
<link href="https://fonts.googleapis.com/css2?family=Montserrat:wght@400;500;700&display=swap" rel="stylesheet">
<style>
  :root {
    --page: #3c3c3c;
    --paper: #ffffff;
    --paper-shade: #f3f3f3;
    --sky: #29a9e0;
    --navy: #114a7e;
    --ink: #2c2c2c;
  }
  * { box-sizing: border-box; margin: 0; padding: 0; }
  html, body { width: 1200px; height: 1200px; overflow: hidden; }
  body {
    background: var(--page);
    font-family: "Montserrat", sans-serif;
    position: relative;
  }
  .card {
    position: absolute;
    left: 180px;
    width: 840px;
    height: 480px;
    border-radius: 30px;
    overflow: hidden;
  }
  .card--front { top: 90px; background: linear-gradient(180deg, var(--paper) 55%, var(--paper-shade)); }
  .card--back { top: 630px; background: var(--navy); }

  .band-light { position: absolute; left: 0; bottom: 0; width: 555px; height: 28px; background: var(--sky); }
  .band-dark { position: absolute; left: 570px; bottom: 0; width: 270px; height: 52px; background: var(--navy); }

  .brand {
    position: absolute;
    display: flex;
    align-items: center;
    gap: 18px;
    font-weight: 700;
    white-space: nowrap;
  }
  .brand__dot { border-radius: 50%; flex: none; }
  .card--front .brand { right: 70px; top: 110px; font-size: 40px; color: var(--navy); }
  .card--front .brand__dot { width: 54px; height: 54px; background: var(--sky); }
  .card--back .brand { left: 50%; top: 50%; transform: translate(-50%, -50%); font-size: 62px; color: var(--paper); }
  .card--back .brand__dot { width: 84px; height: 84px; background: var(--sky); }

  .identity {
    position: absolute;
    left: 70px;
    top: 150px;
    border-left: 7px solid var(--sky);
    padding-left: 16px;
  }
  .identity__name { font-size: 44px; font-weight: 500; color: var(--sky); line-height: 1; letter-spacing: 0.5px; }
  .identity__role { font-size: 20px; font-weight: 400; color: var(--ink); margin-top: 6px; letter-spacing: 0.5px; }

  .contacts {
    position: absolute;
    left: 76px;
    top: 268px;
    list-style: none;
    font-size: 19px;
    color: var(--ink);
  }
  .contacts li { display: flex; align-items: flex-start; gap: 14px; line-height: 1.35; margin-bottom: 6px; }
  .contacts svg { width: 22px; height: 22px; flex: none; margin-top: 2px; fill: var(--sky); }
</style>
</head>
<body>
  <section class="card card--front">
    <div class="brand"><span class="brand__dot"></span>LUMA: Dry Eye</div>

    <div class="identity">
      <p class="identity__name">EVAN HALE</p>
      <p class="identity__role">CEO | FOUNDER</p>
    </div>

    <ul class="contacts">
      <li>
        <svg viewBox="0 0 24 24" aria-hidden="true"><path d="M6.6 10.8a15.2 15.2 0 0 0 6.6 6.6l2.2-2.2c.3-.3.7-.4 1-.2 1.1.4 2.3.6 3.6.6.6 0 1 .4 1 1V20c0 .6-.4 1-1 1A17 17 0 0 1 3 4c0-.6.4-1 1-1h3.5c.6 0 1 .4 1 1 0 1.3.2 2.5.6 3.6.1.3 0 .7-.2 1z"/></svg>
        +1 403-555-0142
      </li>
      <li>
        <svg viewBox="0 0 24 24" aria-hidden="true"><path d="M2 5h20v14H2z M3.5 6.5 12 13l8.5-6.5" stroke="#fff" stroke-width="1.5"/></svg>
        info@lumadryeye.com
      </li>
      <li>
        <svg viewBox="0 0 24 24" aria-hidden="true"><circle cx="12" cy="12" r="10"/><path d="M2 12h20M12 2c3 3 3 17 0 20M12 2c-3 3-3 17 0 20M4 7h16M4 17h16" stroke="#fff" stroke-width="1.2" fill="none"/></svg>
        lumadryeye.com
      </li>
      <li>
        <svg viewBox="0 0 24 24" aria-hidden="true"><path d="M12 2a7 7 0 0 0-7 7c0 5 7 13 7 13s7-8 7-13a7 7 0 0 0-7-7zm0 9.5A2.5 2.5 0 1 1 12 6.5a2.5 2.5 0 0 1 0 5z"/></svg>
        <span>#210 2240 54th Ave SW<br>Calgary, AB T2V 3K8</span>
      </li>
    </ul>

    <div class="band-light"></div>
    <div class="band-dark"></div>
  </section>

  <section class="card card--back">
    <div class="brand"><span class="brand__dot"></span>LUMA: Dry Eye</div>
  </section>
</body>
</html>
```